Family Entertainment Center needs a fundraising flyer design

We need a 8.5 x 5.5 (half sheet of copy paper) flyer designed for a roller skating rink/family entertainment center in Wichita, KS. We partner with 100s of local schools each year by offering PTO fundraisers at our facility. With each party we send out flyers to the schools to send home with each kid to remind them of the time and date of the party as well as get them excited! Most of these schools and PTOs call these fundraisers "skate night".The information we need communicated or on our flyer is below:-Skating $6-Play Zone $6-Skate & Play $10-Skate Rental is included in above pricing-Price is per person-www.pinwheelrollks.com-Pinwheel Roll Center 587 S. Elmridge Ave. Wichita, KS 67219-Our logo (attached)-The words or heading "Skate Night"-A blank, white space for us to print details in (see attached flyer for an example)

Target Market(s)

Elementary School parents and kids

Requirements
Must have
• The information outlined in the description and a blank white space incorporated into the design for our ability to print over.
Nice to have
• colors that match or compliment our logo, creative, but clean fonts

```html
<!DOCTYPE html>
<html lang="en">
<head>
<meta charset="utf-8">
<title>Skate Night Flyer</title>
<link rel="stylesheet" href="https://fonts.googleapis.com/css2?family=Oswald:wght@500;600&family=Montserrat:wght@400;600&display=swap">
<style>
:root{
  --page-bg:#dcdcdc;
  --paper:#ffffff;
  --ink:#333333;
  --brand-red:#b8203a;
  --brand-blue:#3552cc;
  --brand-blue-deep:#2b3fb3;
  --bubble-fill:#e8e9ec;
  --photo-frame:#eeeef2;
}
*{box-sizing:border-box;margin:0;padding:0}
html,body{width:1200px;height:1200px;overflow:hidden;background:var(--page-bg)}
.flyer{position:absolute;left:134px;top:0;width:932px;height:1200px;background:var(--paper);overflow:hidden;font-family:"Montserrat",sans-serif}
.hero-photo{position:absolute;left:30px;top:37px;width:585px;height:504px;background:var(--photo-frame);padding:9px;transform:rotate(-1.5deg)}
.hero-photo .fill{width:100%;height:100%;background:linear-gradient(135deg,#5a1d22 0%,#7c3b3a 35%,#8fb2cf 65%,#3b2c3a 100%)}
.brand{position:absolute;left:683px;top:40px;width:150px;height:140px;display:flex;flex-direction:column;align-items:center;justify-content:center;gap:10px}
.brand-dot{width:34px;height:34px;border-radius:50%;background:var(--brand-blue)}
.brand-name{font-family:"Oswald",sans-serif;font-weight:600;font-size:26px;color:var(--brand-blue);text-transform:uppercase;letter-spacing:1px;text-align:center;line-height:1}
.headline{position:absolute;left:650px;top:192px;font-family:"Oswald",sans-serif;font-weight:600;font-size:94px;line-height:88px;color:var(--ink);letter-spacing:1px}
.bubble{position:absolute;left:75px;top:528px;width:779px;height:442px}
.prices{position:absolute;left:539px;top:375px;width:362px;height:201px;border:4px solid var(--brand-red);border-radius:14px;background:linear-gradient(180deg,var(--brand-blue) 0%,var(--brand-blue-deep) 100%);color:#fff;box-shadow:0 0 0 4px var(--paper)}
.price-row{display:flex;padding:20px 10px 0}
.price{flex:1;text-align:center}
.price + .price{border-left:2px dotted rgba(255,255,255,.8)}
.price-label{font-family:"Oswald",sans-serif;font-weight:500;font-size:17px;letter-spacing:.3px}
.price-value{font-family:"Oswald",sans-serif;font-weight:600;font-size:48px;line-height:56px}
.price-note{padding:18px 24px 0;font-size:17px;line-height:22px}
.footer-band{position:absolute;left:0;top:1086px;width:932px;height:114px;background:var(--brand-red)}
.gallery{position:absolute;left:51px;top:970px;width:829px;height:156px;background:var(--paper);display:flex;gap:12px;padding:7px 10px 12px 11px}
.gallery-photo{flex:1}
.gallery-photo.play{background:linear-gradient(135deg,#2c2a55,#c9435a 60%,#3b8a5a)}
.gallery-photo.climb{background:linear-gradient(135deg,#1f3d4f,#2f6a66 50%,#5a6fae)}
.gallery-photo.group{background:linear-gradient(135deg,#6d4a4a,#b3473e 50%,#52426a)}
.footer-info{position:absolute;left:0;top:1133px;width:932px;display:flex;justify-content:space-between;align-items:center;padding:0 42px 0 40px;color:#fff;font-size:18px}
.footer-item{display:flex;align-items:center;gap:12px}
</style>
</head>
<body>
<main class="flyer">
  <div class="hero-photo"><div class="fill" role="img" aria-label="Photo of three smiling girls playing an arcade game at the skate center"></div></div>

  <div class="brand">
    <span class="brand-dot"></span>
    <span class="brand-name">Pinwheel Roll</span>
  </div>

  <h1 class="headline">SKATE<br>NIGHT</h1>

  <svg class="bubble" viewBox="-6 -6 885 510" preserveAspectRatio="none" aria-hidden="true">
    <path d="M20,170 C0,110 80,50 200,70 C210,20 350,-10 470,20 C520,0 560,10 600,40 C700,40 780,60 780,120 C860,140 890,220 860,290 C880,340 820,380 760,370 C740,420 680,425 608,420 L463,492 C480,470 495,445 493,420 C380,430 200,430 170,370 C60,380 0,300 40,250 C0,230 0,190 20,170 Z" fill="var(--bubble-fill)" stroke="var(--ink)" stroke-width="4" stroke-linejoin="round"/>
  </svg>

  <section class="prices">
    <div class="price-row">
      <div class="price"><div class="price-label">SKATING</div><div class="price-value">$6</div></div>
      <div class="price"><div class="price-label">PLAY ZONE</div><div class="price-value">$6</div></div>
      <div class="price"><div class="price-label">SKATE &amp; PLAY</div><div class="price-value">$10</div></div>
    </div>
    <p class="price-note">Skate Rental is included in above pricing-Price is per person</p>
  </section>

  <div class="footer-band"></div>
  <div class="gallery">
    <div class="gallery-photo play" role="img" aria-label="Photo of girls playing in the soft play zone"></div>
    <div class="gallery-photo climb" role="img" aria-label="Photo of a boy climbing in the play structure"></div>
    <div class="gallery-photo group" role="img" aria-label="Photo of a group of cheering kids at the party"></div>
  </div>

  <footer class="footer-info">
    <div class="footer-item">
      <svg width="22" height="30" viewBox="0 0 22 30" aria-hidden="true"><path d="M11 2a8 8 0 0 0-8 8c0 6 8 14 8 14s8-8 8-14a8 8 0 0 0-8-8z" fill="none" stroke="#fff" stroke-width="2"/><circle cx="11" cy="10" r="3" fill="none" stroke="#fff" stroke-width="2"/><ellipse cx="11" cy="27" rx="8" ry="2" fill="none" stroke="#fff" stroke-width="1.5"/></svg>
      <span>Pinwheel Roll Center 587 S. Elmridge Ave. Wichita, KS 67219</span>
    </div>
    <div class="footer-item">
      <svg width="22" height="22" viewBox="0 0 22 22" aria-hidden="true"><g fill="none" stroke="#fff" stroke-width="1.8"><circle cx="11" cy="11" r="9.5"/><ellipse cx="11" cy="11" rx="4" ry="9.5"/><path d="M1.5 11h19M3 6h16M3 16h16"/></g></svg>
      <span>www.pinwheelrollks.com</span>
    </div>
  </footer>
</main>
</body>
</html>
```